Build a Web page - Dorian Pellway Homes, LLC - a custom home builder

We are a custom home builder in Wisconsin. Need a basic web page with a home page, About Us, Contact info, Gallery, and Testimonials page. Gallery will probably have sub-pages and each will have about ten pictures or less. I already own the domain and have web hosting through Wix, I just need the site built. Once the page is built I should be able to do the upkeep on it myself. If I need to add pictures or whatever.
Updates

Project Deadline Extended
Reason: I am still looking through designs and will select soon - thank you!

Target Market(s)

Gen X and Millennials who are looking to build a home. Custom built homes - not generic spec homes.

Industry/Entity Type

Home Builder

Number of Pages Required

5+ page

Font styles to use
Sans Serif

Colors
ffffff
ec1f27
000000
9d9d9d

Requirements
Must have
• I have no idea if I want coded or in coded. I'm not sure of the difference and why I would want one over the other.
Nice to have
• We like the following colors - red, black, gray, white.
Should not have
• not a big fan of clip art like hammers, tape measures, etc. Must look professional.

```html
<!DOCTYPE html>
<html lang="en">
<head>
<meta charset="utf-8">
<title>Dorian Pellway Homes, LLC</title>
<link rel="stylesheet" href="https://fonts.googleapis.com/css2?family=Roboto:ital,wght@0,400;0,500;0,700;1,400&display=swap">
<style>
:root{
  --red:#c8161f;
  --red-dark:#a10f17;
  --black:#1b1b1b;
  --charcoal:#2a2a2a;
  --grey:#9d9d9d;
  --light:#e6e6e6;
  --panel:#efefef;
  --white:#ffffff;
  --text:#3a3a3a;
}
*{box-sizing:border-box;margin:0;padding:0}
html,body{width:1200px;height:3403px;overflow:hidden}
body{font-family:'Roboto',Arial,sans-serif;color:var(--text);background:var(--white);position:relative}
svg{display:block}

.topbar{height:24px;background:var(--red);color:var(--white);font-size:10px;display:flex;align-items:center;justify-content:space-between;padding:0 175px}
.topbar span{display:flex;align-items:center;gap:6px}

.site-header{height:82px;display:flex;align-items:center;justify-content:space-between;padding:0 175px;border-bottom:4px solid #d7d7d7}
.brand{display:flex;align-items:center;gap:10px}
.brand-square{width:18px;height:18px;background:var(--red)}
.brand-name{font-size:15px;font-weight:700;color:var(--black);letter-spacing:.3px}
.main-nav{display:flex;gap:22px;font-size:12px;font-weight:700;color:var(--black);text-transform:uppercase}
.main-nav .active{border-bottom:2px solid var(--red);padding-bottom:3px}

.hero{position:relative;height:468px;background:linear-gradient(180deg,#9fb7cf 0%,#c9d6e1 35%,#5f6a5a 55%,#6a8a3e 78%,#b8b8b4 100%)}
.hero-card{position:absolute;left:662px;top:118px;width:363px;height:211px;background:rgba(190,20,30,.82);border-radius:8px;color:var(--white);text-align:center;padding:26px 16px}
.hero-card h1{font-size:29px;font-weight:700;line-height:1;text-transform:uppercase;white-space:nowrap}
.hero-card h2{font-size:22px;font-weight:400;text-transform:uppercase;margin-top:2px;white-space:nowrap}
.hero-card p{font-size:12px;line-height:1.4;margin:8px auto 0;width:240px}
.btn-dark{display:inline-flex;align-items:center;gap:6px;background:var(--black);color:var(--white);font-size:12px;font-weight:700;text-transform:uppercase;padding:9px 18px;margin-top:14px;border-radius:2px}

.services{display:flex;justify-content:space-between;width:853px;margin:45px auto 0}
.service{width:270px;height:352px;border:3px solid var(--red);text-align:center}
.service .photo{height:166px}
.service h3{font-size:16px;font-weight:700;color:var(--black);text-transform:uppercase;margin-top:22px}
.service p{font-size:11px;line-height:1.5;margin:14px 24px 0}
.btn-small{display:inline-flex;align-items:center;gap:5px;background:var(--black);color:var(--white);font-size:10px;font-weight:700;text-transform:uppercase;padding:7px 14px;margin-top:14px}

.section-title{text-align:center;font-size:28px;font-weight:700;color:var(--black);text-transform:uppercase}
.ornament{width:560px;margin:10px auto 0}

.welcome{margin-top:46px}
.welcome p{width:853px;margin:24px auto 0;text-align:center;font-size:10.5px;line-height:1.75}

.call-band{height:166px;margin-top:50px;background:linear-gradient(90deg,#262626,#3c3c3c 50%,#262626);text-align:center;color:var(--white);padding-top:35px}
.call-band h2{font-size:28px;font-weight:700;text-transform:uppercase}
.btn-red{display:inline-flex;align-items:center;gap:6px;background:var(--red);color:var(--white);font-size:16px;font-weight:700;text-transform:uppercase;padding:8px 28px;border-radius:20px;margin-top:20px}

.listings{margin-top:40px}
.listing-row{display:flex;justify-content:space-between;width:853px;margin:30px auto 0}
.listing{width:270px;background:var(--panel)}
.listing .photo{height:166px}
.listing-bar{height:38px;background:var(--red);color:var(--white);display:flex;align-items:center;justify-content:space-between;padding:0 10px;font-size:10px;position:relative}
.listing-bar span{display:flex;align-items:center;gap:5px}
.listing-bar strong{font-weight:700}
.listing-bar::after{content:"";position:absolute;left:50%;bottom:-8px;margin-left:-8px;border:8px solid transparent;border-bottom:0;border-top-color:var(--red)}
.listing h4{text-align:center;font-size:14px;font-weight:700;color:var(--black);margin-top:28px}
.listing p{text-align:center;font-size:10px;line-height:1.55;margin:14px 24px 0;height:84px}
.listing-meta{height:41px;background:var(--charcoal);color:var(--white);display:flex;align-items:center;justify-content:space-between;padding:0 12px;font-size:10px}
.listing-meta span{display:flex;align-items:center;gap:5px}

.gallery{margin-top:45px}
.gallery-grid{display:grid;grid-template-columns:465px 351px 352px;grid-template-rows:245px 248px;column-gap:16px;row-gap:13px;margin-top:36px}
.gallery-grid .photo{position:relative}
.drop-overlay{position:absolute;inset:0;display:flex;align-items:center;justify-content:center}
.drop-card{width:290px;height:200px;background:rgba(190,20,30,.85);border:2px solid rgba(255,255,255,.5);outline:10px solid rgba(190,20,30,.85);text-align:center;color:var(--white);padding-top:34px}
.drop-card h5{font-size:14px;font-weight:700;text-transform:uppercase;margin-top:10px}
.drop-card p{font-size:10px;line-height:1.5;margin:8px 40px 0}

.testimonials{margin-top:56px}
.quote-box{position:relative;width:853px;height:206px;margin:44px auto 0;background:var(--light);text-align:center;padding:46px 60px 0}
.quote-box blockquote{font-size:12px;font-style:italic;line-height:1.6;color:var(--text)}
.quote-box cite{display:block;font-style:normal;font-size:10px;margin-top:16px}
.quote-mark{font-size:24px;font-weight:700;font-style:normal;color:var(--black);vertical-align:-4px}
.quote-person{position:absolute;left:50%;top:156px;margin-left:-42px;width:84px}
.quote-person .photo{width:84px;height:86px;border:4px solid var(--white)}
.quote-arrow{position:absolute;top:39px}

.contact{position:absolute;left:0;top:3010px;width:1200px;height:347px;background:linear-gradient(180deg,#1e1e1e,#2b2b2b);color:var(--white);text-align:center;padding-top:30px}
.contact h2{font-size:28px;font-weight:700;text-transform:uppercase;margin-top:12px}
.contact .sub{font-size:11px;margin-top:6px}
.contact-form{display:flex;justify-content:space-between;width:853px;margin:22px auto 0}
.contact-form .inputs{display:flex;flex-direction:column;gap:13px;width:422px}
.field{height:28px;background:#d9d9d9;color:#777;font-size:9px;text-align:left;padding:9px 10px}
.field.message{width:399px;height:109px}
.btn-submit{display:inline-block;background:var(--red);color:var(--white);font-size:16px;font-weight:700;text-transform:uppercase;padding:7px 26px;margin-top:28px}

.site-footer{position:absolute;left:0;top:3357px;width:1200px;height:46px;background:var(--red);color:var(--white);display:flex;align-items:center;justify-content:space-between;padding:0 175px;font-size:11px}
.site-footer nav{display:flex;gap:12px}
.social{display:flex;gap:9px}
.social span{width:22px;height:22px;border:1.5px solid var(--white);border-radius:50%}
</style>
</head>
<body>

<div class="topbar">
  <span><svg width="10" height="13" viewBox="0 0 10 13"><path d="M5 0a5 5 0 0 0-5 5c0 3.5 5 8 5 8s5-4.5 5-8a5 5 0 0 0-5-5zm0 7a2 2 0 1 1 0-4 2 2 0 0 1 0 4z" fill="#fff"/></svg>4120 Alder Ridge Road, Madison, WI 53704</span>
  <span><svg width="12" height="12" viewBox="0 0 12 12"><path d="M2.4 0.5l2 2.3-1.2 1.5c.8 1.7 2.2 3.1 3.9 3.9l1.5-1.2 2.3 2-1 2.3C5.3 11.3.7 6.7.2 1.5z" fill="#fff"/></svg>+1 800 555 0142</span>
</div>

<header class="site-header">
  <div class="brand"><span class="brand-square"></span><span class="brand-name">Dorian Pellway Homes</span></div>
  <nav class="main-nav">
    <span class="active">Home</span><span>About Us</span><span>Gallery</span><span>Testimonials</span><span>Contact Us</span>
  </nav>
</header>

<section class="hero" role="img" aria-label="Two-storey green-sided family home with stone entry, lawn and driveway under a blue sky">
  <div class="hero-card">
    <h1>Finding Your House</h1>
    <h2>Is Much Easier Now!</h2>
    <p>Lorem Ipsum is simply dummy text of the printing and typesetting industry. Lorem Ipsum industry.</p>
    <span class="btn-dark">Read More
      <svg width="12" height="12" viewBox="0 0 12 12"><circle cx="6" cy="6" r="6" fill="#fff"/><path d="M5 3.5L7.5 6 5 8.5" stroke="#1b1b1b" stroke-width="1.6" fill="none"/></svg></span>
  </div>
</section>

<section class="services">
  <article class="service">
    <div class="photo" role="img" aria-label="Two-storey custom home with porch" style="background:linear-gradient(180deg,#e9eef3,#b9a7a1 55%,#7d8f5c)"></div>
    <h3>Custom Home</h3>
    <p>typesetting industry. Lorem Ipsum has been the survived not only five centuries, but also the leap remaining essentially unchanged.</p>
    <span class="btn-small">Read More <svg width="10" height="10" viewBox="0 0 12 12"><circle cx="6" cy="6" r="6" fill="#fff"/><path d="M5 3.5L7.5 6 5 8.5" stroke="#1b1b1b" stroke-width="1.6" fill="none"/></svg></span>
  </article>
  <article class="service">
    <div class="photo" role="img" aria-label="Bedroom with wooden bed and patterned quilt" style="background:linear-gradient(180deg,#c9b7a0,#8a5a3e 55%,#b7524a)"></div>
    <h3>Residential Home</h3>
    <p>typesetting industry. Lorem Ipsum has been the survived not only five centuries, but also the leap remaining essentially unchanged.</p>
    <span class="btn-small">Read More <svg width="10" height="10" viewBox="0 0 12 12"><circle cx="6" cy="6" r="6" fill="#fff"/><path d="M5 3.5L7.5 6 5 8.5" stroke="#1b1b1b" stroke-width="1.6" fill="none"/></svg></span>
  </article>
  <article class="service">
    <div class="photo" role="img" aria-label="Kitchen with wooden cabinets and island" style="background:linear-gradient(180deg,#8c5a35,#6b3f24 50%,#a08470)"></div>
    <h3>Commercial Home</h3>
    <p>typesetting industry. Lorem Ipsum has been the survived not only five centuries, but also the leap remaining essentially unchanged.</p>
    <span class="btn-small">Read More <svg width="10" height="10" viewBox="0 0 12 12"><circle cx="6" cy="6" r="6" fill="#fff"/><path d="M5 3.5L7.5 6 5 8.5" stroke="#1b1b1b" stroke-width="1.6" fill="none"/></svg></span>
  </article>
</section>

<section class="welcome">
  <h2 class="section-title">Welcome to Dorian Pellway Homes</h2>
  <svg class="ornament" width="560" height="14" viewBox="0 0 560 14"><line x1="0" y1="7" x2="250" y2="7" stroke="#ddd"/><line x1="310" y1="7" x2="560" y2="7" stroke="#ddd"/><polygon points="265,4 266.5,7 265,10 263.5,7" fill="#444"/><polygon points="295,4 296.5,7 295,10 293.5,7" fill="#444"/><polygon points="280,0 282.2,5 287.5,5.3 283.4,8.6 284.8,14 280,11 275.2,14 276.6,8.6 272.5,5.3 277.8,5" fill="var(--red)"/></svg>
  <p>Lorem Ipsum is simply dummy text of the printing and typesetting industry. Lorem Ipsum has been the industry's standard dummy text ever since the 1500s, when an unknown printer took a galley of type and scrambled it to make a type specimen book. It has survived not only five centuries, but also the leap into electronic typesetting, remaining essentially unchanged. It was popularised in the 1960s with the release of printed sheets containing Lorem Ipsum passages, and more recently with desktop publishing software including versions of Lorem Ipsum</p>
</section>

<section class="call-band">
  <h2>Helping You Find a Place You Can Call Home</h2>
  <span class="btn-red">Contact Us <svg width="13" height="13" viewBox="0 0 12 12"><circle cx="6" cy="6" r="6" fill="#fff"/><path d="M5 3.5L7.5 6 5 8.5" stroke="#c8161f" stroke-width="1.6" fill="none"/></svg></span>
</section>

<section class="listings">
  <h2 class="section-title">Viewed Listings</h2>
  <svg class="ornament" width="560" height="14" viewBox="0 0 560 14"><line x1="0" y1="7" x2="250" y2="7" stroke="#ddd"/><line x1="310" y1="7" x2="560" y2="7" stroke="#ddd"/><polygon points="265,4 266.5,7 265,10 263.5,7" fill="#444"/><polygon points="295,4 296.5,7 295,10 293.5,7" fill="#444"/><polygon points="280,0 282.2,5 287.5,5.3 283.4,8.6 284.8,14 280,11 275.2,14 276.6,8.6 272.5,5.3 277.8,5" fill="var(--red)"/></svg>
  <div class="listing-row">
    <article class="listing">
      <div class="photo" role="img" aria-label="Ranch home with stone patio and outdoor seating" style="background:linear-gradient(180deg,#cfd8e0,#b8a993 50%,#7b8e4a)"></div>
      <div class="listing-bar"><span><svg width="9" height="12" viewBox="0 0 10 13"><path d="M5 0a5 5 0 0 0-5 5c0 3.5 5 8 5 8s5-4.5 5-8a5 5 0 0 0-5-5zm0 7a2 2 0 1 1 0-4 2 2 0 0 1 0 4z" fill="#fff"/></svg>Lorem Ipsum simply dummy text</span><strong>$479,500</strong></div>
      <h4>Lorem Ipsum is simply</h4>
      <p>Lorem Ipsum is simply dummy text of the printing and typesetting industry. Lorem Ipsum has been the industry's standard dummy</p>
      <div class="listing-meta">
        <span><svg width="9" height="11" viewBox="0 0 9 11"><path d="M0 0h9v11L4.5 8 0 11z" fill="#fff"/></svg>870 ft2</span>
        <span><svg width="16" height="10" viewBox="0 0 16 10"><path d="M0 0v10h1.5V8h13v2H16V5H5V3H1.5V0zM2 2.5a1.3 1.3 0 1 0 0 .1z" fill="#fff"/></svg>2 bedrooms</span>
        <span><svg width="13" height="11" viewBox="0 0 13 11"><path d="M0 5h13v2c0 2-1.5 3-3 3H3C1.5 10 0 9 0 7zM2 4V1.5a1.5 1.5 0 0 1 3 0" fill="#fff" stroke="#fff"/></svg>2 baths</span>
      </div>
    </article>
    <article class="listing">
      <div class="photo" role="img" aria-label="Home exterior with wooden deck and railing" style="background:linear-gradient(180deg,#dfe4e6,#b3a79a 45%,#8a4c3c 70%,#6f8b45)"></div>
      <div class="listing-bar"><span><svg width="9" height="12" viewBox="0 0 10 13"><path d="M5 0a5 5 0 0 0-5 5c0 3.5 5 8 5 8s5-4.5 5-8a5 5 0 0 0-5-5zm0 7a2 2 0 1 1 0-4 2 2 0 0 1 0 4z" fill="#fff"/></svg>Lorem Ipsum simply dummy text</span><strong>$479,500</strong></div>
      <h4>Lorem Ipsum is simply</h4>
      <p>Lorem Ipsum is simply dummy text of the printing and typesetting industry. Lorem Ipsum has been the industry's standard dummy</p>
      <div class="listing-meta">
        <span><svg width="9" height="11" viewBox="0 0 9 11"><path d="M0 0h9v11L4.5 8 0 11z" fill="#fff"/></svg>870 ft2</span>
        <span><svg width="16" height="10" viewBox="0 0 16 10"><path d="M0 0v10h1.5V8h13v2H16V5H5V3H1.5V0zM2 2.5a1.3 1.3 0 1 0 0 .1z" fill="#fff"/></svg>2 bedrooms</span>
        <span><svg width="13" height="11" viewBox="0 0 13 11"><path d="M0 5h13v2c0 2-1.5 3-3 3H3C1.5 10 0 9 0 7zM2 4V1.5a1.5 1.5 0 0 1 3 0" fill="#fff" stroke="#fff"/></svg>2 baths</span>
      </div>
    </article>
    <article class="listing">
      <div class="photo" role="img" aria-label="Living room with red sofas and fireplace" style="background:linear-gradient(180deg,#c7b9a6,#8a6a55 50%,#7a3a30)"></div>
      <div class="listing-bar"><span><svg width="9" height="12" viewBox="0 0 10 13"><path d="M5 0a5 5 0 0 0-5 5c0 3.5 5 8 5 8s5-4.5 5-8a5 5 0 0 0-5-5zm0 7a2 2 0 1 1 0-4 2 2 0 0 1 0 4z" fill="#fff"/></svg>Lorem Ipsum simply dummy text</span><strong>$479,500</strong></div>
      <h4>Lorem Ipsum is simply</h4>
      <p>Lorem Ipsum is simply dummy text of the printing and typesetting industry. Lorem Ipsum has been the industry's standard dummy</p>
      <div class="listing-meta">
        <span><svg width="9" height="11" viewBox="0 0 9 11"><path d="M0 0h9v11L4.5 8 0 11z" fill="#fff"/></svg>870 ft2</span>
        <span><svg width="16" height="10" viewBox="0 0 16 10"><path d="M0 0v10h1.5V8h13v2H16V5H5V3H1.5V0zM2 2.5a1.3 1.3 0 1 0 0 .1z" fill="#fff"/></svg>2 bedrooms</span>
        <span><svg width="13" height="11" viewBox="0 0 13 11"><path d="M0 5h13v2c0 2-1.5 3-3 3H3C1.5 10 0 9 0 7zM2 4V1.5a1.5 1.5 0 0 1 3 0" fill="#fff" stroke="#fff"/></svg>2 baths</span>
      </div>
    </article>
  </div>
</section>

<section class="gallery">
  <h2 class="section-title">Our Gallery</h2>
  <svg class="ornament" width="560" height="14" viewBox="0 0 560 14"><line x1="0" y1="7" x2="250" y2="7" stroke="#ddd"/><line x1="310" y1="7" x2="560" y2="7" stroke="#ddd"/><polygon points="265,4 266.5,7 265,10 263.5,7" fill="#444"/><polygon points="295,4 296.5,7 295,10 293.5,7" fill="#444"/><polygon points="280,0 282.2,5 287.5,5.3 283.4,8.6 284.8,14 280,11 275.2,14 276.6,8.6 272.5,5.3 277.8,5" fill="var(--red)"/></svg>
  <div class="gallery-grid">
    <div class="photo" role="img" aria-label="Backyard stone patio with table and trees" style="background:linear-gradient(180deg,#d5dde3,#b4a48c 45%,#6f8646)"></div>
    <div class="photo" role="img" aria-label="Interior room photo" style="background:linear-gradient(180deg,#6b4a38,#3b3a36)">
      <div class="drop-overlay">
        <div class="drop-card">
          <svg width="34" height="34" viewBox="0 0 34 34" style="margin:0 auto"><circle cx="14" cy="14" r="11" fill="none" stroke="#fff" stroke-width="2"/><line x1="22" y1="22" x2="32" y2="32" stroke="#fff" stroke-width="3"/><path d="M14 9v10M9 14h10" stroke="#fff" stroke-width="2"/></svg>
          <h5>Drag and Drop</h5>
          <p>Sed ut perspiciatis unde omnis iste natus error sit voluptatem ut perspiciatis</p>
        </div>
      </div>
    </div>
    <div class="photo" role="img" aria-label="Bathroom with white cabinets and wall TV" style="background:linear-gradient(180deg,#e6e4e0,#c9c4bc 60%,#9f9a92)"></div>
    <div class="photo" role="img" aria-label="Wooden staircase with railing" style="background:linear-gradient(135deg,#e3ddd2,#a8714a 55%,#6b3f22)"></div>
    <div class="photo" role="img" aria-label="Mudroom lockers with hooks and benches" style="background:linear-gradient(180deg,#b07a4c,#8a5a36 60%,#5c3b23)"></div>
    <div class="photo" role="img" aria-label="Hallway with wooden doors and window" style="background:linear-gradient(90deg,#7a4a2a,#d8d2c8 50%,#8f5e3a)"></div>
  </div>
</section>

<section class="testimonials">
  <h2 class="section-title">Testimonials</h2>
  <div class="quote-box">
    <blockquote><span class="quote-mark">&ldquo;</span> Lorem Ipsum is simply dummy text of the printing and typesetting industry. Lorem Ipsum has been the industry's standard dummy text ever since the 1500s, when an unknown printer took a galley of type and scrambled it to make a type specimen book. It has survived not only five centuries, but also the leap into electronic typesetting, remaining essentially unchanged. <span class="quote-mark">&rdquo;</span></blockquote>
    <cite>-Jenna Holloway</cite>
    <div class="quote-person">
      <svg class="quote-arrow" width="14" height="8" viewBox="0 0 14 8" style="left:-24px"><path d="M14 4H1M4 1L1 4l3 3" stroke="#333" fill="none"/></svg>
      <div class="photo" role="img" aria-label="Portrait of the client giving the testimonial" style="background:linear-gradient(180deg,#c9a98e,#6b5a4e)"></div>
      <svg class="quote-arrow" width="14" height="8" viewBox="0 0 14 8" style="right:-24px"><path d="M0 4h13M10 1l3 3-3 3" stroke="#333" fill="none"/></svg>
    </div>
  </div>
</section>

<section class="contact">
  <svg width="22" height="16" viewBox="0 0 22 16" style="margin:0 auto"><rect x="1" y="1" width="20" height="14" rx="1" fill="none" stroke="#fff" stroke-width="1.6"/><path d="M1 1l10 8 10-8" fill="none" stroke="#fff" stroke-width="1.6"/></svg>
  <h2>Get in Touch With Us</h2>
  <p class="sub">Feel Free to Contact with us</p>
  <div class="contact-form">
    <div class="inputs">
      <div class="field">Enter your name...</div>
      <div class="field">Enter your email...</div>
      <div class="field">Enter your phone...</div>
    </div>
    <div class="field message">Enter your comments...</div>
  </div>
  <span class="btn-submit">Submit</span>
</section>

<footer class="site-footer">
  <nav><span>Home</span><span>About Us</span><span>Gallery</span><span>Testimonials</span><span>Contact Us</span></nav>
  <div class="social"><span></span><span></span><span></span><span></span><span></span></div>
</footer>

</body>
</html>
```